Harbour Crest Physiotherapy Website www.harbourcrestphysiotherapy.com.au

Create Wordpress website for Harbour Crest Physiotherapy which aligns with our other locations www.maplebendphysiotherapy,com.au. We would like the website to present in a similar fashion to our exisiting site with similar headings and layout. We will then alter the text to make it location specific.

Coding

Coded - Design and coding required

Number of Pages Required

1 page

Font styles to use
Sans Serif

Requirements
Must have
• Colours of the website must match the colours of the colour Harbour Crest Physiotherapy logo
• Website must be complimentary to existing websites,
• www.maplebendphysiotherapy.com.au
• www.maplebendpilatesandrehab.com.au

```html
<!DOCTYPE html>
<html lang="en">
<head>
<meta charset="utf-8">
<title>Harbour Crest Physiotherapy</title>
<link href="https://fonts.googleapis.com/css2?family=Roboto:wght@400;500;700&family=Roboto+Condensed:wght@400;700&display=swap" rel="stylesheet">
<style>
:root{
  --navy:#2c2e68;
  --navy-deep:#24265a;
  --green:#7cbca3;
  --green-soft:#8ec8b1;
  --ink:#333;
  --muted:#555;
  --white:#fff;
  --footer:#f3f3f4;
}
*{margin:0;padding:0;box-sizing:border-box}
html,body{width:1200px;height:3152px;overflow:hidden}
body{position:relative;font-family:"Roboto",sans-serif;color:var(--ink);background:var(--white)}
.abs{position:absolute}
/* header */
.site-header{left:0;top:0;width:1200px;height:120px;background:var(--white)}
.brand{left:100px;top:30px;display:flex;align-items:center;gap:12px;font-family:"Roboto Condensed",sans-serif;font-weight:700;font-size:24px;color:var(--navy);line-height:1.05;width:300px}
.brand-dot{width:42px;height:42px;border-radius:50%;background:var(--navy);flex:none}
.callus{left:588px;top:24px;font-family:"Roboto Condensed",sans-serif;font-weight:700;font-size:21px;color:var(--navy);display:flex;align-items:center;gap:8px}
.search{left:846px;top:16px;width:254px;height:38px;border:1px solid #bbb;border-radius:19px;font-size:13px;color:#999;padding:10px 18px}
.search svg{position:absolute;right:12px;top:9px}
.main-nav{left:444px;top:80px;display:flex;gap:25px;font-family:"Roboto Condensed",sans-serif;font-size:18px;color:var(--navy-deep);font-weight:500}
/* hero */
.hero{left:0;top:120px;width:1200px;height:600px}
.hero-photo{left:0;top:0;width:1200px;height:600px;background:linear-gradient(120deg,#8c6a5a,#c9a48e 35%,#6f6a80 60%,#b58a86)}
.hero-title{left:0;top:442px;width:1200px;text-align:center;color:var(--white);font-family:"Roboto Condensed",sans-serif;font-weight:700;line-height:1;text-shadow:0 2px 6px rgba(0,0,0,.25)}
.hero-title span{display:block;font-size:46px}
.hero-title strong{display:block;font-size:72px;margin-top:4px}
.arrow{top:252px;width:30px;height:30px;border-radius:50%;background:rgba(0,0,0,.6)}
/* welcome */
.welcome-photo{left:105px;top:790px;width:320px;height:320px;border-radius:50%;border:6px solid #b9c3de;background:linear-gradient(135deg,#d9e0e4,#7fb9a0 60%,#3f6f5a)}
.welcome-text{left:488px;top:790px;width:580px}
.welcome-text h1{font-family:"Roboto Condensed",sans-serif;font-weight:700;font-size:32px;color:var(--navy);line-height:1.15}
.welcome-text p{font-size:12.5px;line-height:1.85;color:var(--muted);margin-top:16px}
.btn{display:inline-block;font-family:"Roboto Condensed",sans-serif;font-weight:700;font-size:15px;color:var(--white);padding:10px 15px;border-radius:3px}
.btn-green{background:var(--green);margin-top:20px}
/* services */
.services{left:0;top:1198px;width:1200px;height:746px;background:var(--navy)}
.section-title{width:100%;text-align:center;font-family:"Roboto Condensed",sans-serif;font-weight:700;font-size:34px}
.services .section-title{position:absolute;top:55px;color:var(--white)}
.service{width:320px;text-align:center;color:var(--white)}
.service .icon{width:122px;height:122px;margin:0 auto;border-radius:50%;border:3px solid var(--white);background:var(--green);display:flex;align-items:center;justify-content:center}
.service h3{font-family:"Roboto Condensed",sans-serif;font-weight:500;font-size:17.5px;margin-top:18px}
.service p{font-size:12.5px;line-height:1.85;margin-top:12px;padding:0 14px}
/* practitioners */
.practitioners{left:0;top:1944px;width:1200px;height:343px;background:var(--green-soft);color:var(--white);text-align:center}
.practitioners .section-title{position:absolute;top:80px}
.practitioners p{position:absolute;left:205px;top:136px;width:790px;font-size:15px;line-height:1.75}
.btn-navy{background:var(--navy);border-radius:18px;font-size:13px;padding:9px 26px}
/* blog */
.blog-title{top:2350px;color:#222}
.post{width:311px}
.post-photo{width:311px;height:179px}
.post-date{position:absolute;right:10px;top:0;width:44px;background:var(--green);color:var(--white);text-align:center;font-family:"Roboto Condensed",sans-serif;font-size:14px;line-height:1.15;padding:6px 0}
.post h3{font-weight:400;font-size:18px;color:#222;margin-top:24px}
.post p{font-size:11.5px;line-height:1.7;color:var(--muted);margin-top:10px}
/* footer */
.site-footer{left:0;top:2795px;width:1200px;height:295px;background:var(--footer)}
.footer-brand{left:100px;top:70px;font-family:"Roboto Condensed",sans-serif;font-weight:700;font-size:20px;color:var(--navy);display:flex;gap:10px;align-items:center;width:190px;line-height:1.05}
.footer-brand .brand-dot{width:34px;height:34px}
.social{top:150px;width:40px;height:40px;border-radius:50%;border:2px solid #5c74b8}
.col-title{font-family:"Roboto Condensed",sans-serif;font-weight:700;font-size:21px;color:#222}
.contact-list{list-style:none;margin-top:22px;font-size:13.5px;color:#444;line-height:1.7}
.contact-list li{display:flex;gap:12px;margin-bottom:14px}
.contact-list svg{flex:none;margin-top:3px}
.newsletter p{font-size:11.5px;line-height:1.7;color:#444;margin-top:18px}
.email-field{margin-top:16px;width:280px;height:42px;background:var(--white);border:1px solid #ddd;font-size:11.5px;color:#777;padding:13px 14px}
.btn-sub{background:var(--navy);font-size:13px;padding:12px 14px;margin-top:12px;border-radius:0}
.quick-links{list-style:none;margin-top:24px;font-size:12.5px;color:#333;line-height:1.7}
.quick-links li::before{content:"";display:inline-block;border-left:5px solid #222;border-top:4px solid transparent;border-bottom:4px solid transparent;margin-right:10px}
.copyright{left:0;top:3090px;width:1200px;height:62px;border-top:1px solid #ddd;text-align:center;font-size:12.5px;color:#444;padding-top:22px}
</style>
</head>
<body>

<header class="site-header abs">
  <div class="brand abs"><span class="brand-dot"></span>Harbour Crest Physiotherapy</div>
  <div class="callus abs">
    <svg width="18" height="18" viewBox="0 0 24 24"><path fill="#2c2e68" d="M6.6 10.8a15 15 0 006.6 6.6l2.2-2.2a1 1 0 011-.25 11 11 0 003.6.6 1 1 0 011 1V20a1 1 0 01-1 1A17 17 0 013 4a1 1 0 011-1h3.5a1 1 0 011 1 11 11 0 00.6 3.6 1 1 0 01-.25 1z"/></svg>
    CALLUS : 03 9555 0142
  </div>
  <div class="search abs">Search here
    <svg width="18" height="18" viewBox="0 0 24 24"><circle cx="10" cy="10" r="7" fill="none" stroke="#999" stroke-width="2.4"/><path d="M15 15l6 6" stroke="#999" stroke-width="2.4"/></svg>
  </div>
  <nav class="main-nav abs"><span>HOME</span><span>ABOUT</span><span>SERVICES</span><span>CONDITIONS</span><span>HEALTH TIPS</span><span>BLOG</span><span>CONTACT</span></nav>
</header>

<section class="hero abs">
  <div class="hero-photo abs" role="img" aria-label="Women doing floor exercises on mats in a bright studio class"></div>
  <svg class="abs" style="left:0;top:430px" width="1200" height="180" viewBox="0 0 1200 180">
    <path d="M0 100 Q600 245 1200 100 L1200 180 L0 180Z" fill="#fff"/>
    <path d="M0 108 Q600 250 1200 100 Q600 232 0 108Z" fill="#2c2e68" stroke="#2c2e68" stroke-width="3"/>
  </svg>
  <div class="arrow abs" style="left:68px"><svg width="30" height="30"><path d="M17 9l-6 6 6 6" stroke="#fff" stroke-width="2.5" fill="none"/></svg></div>
  <div class="arrow abs" style="left:1102px"><svg width="30" height="30"><path d="M13 9l6 6-6 6" stroke="#fff" stroke-width="2.5" fill="none"/></svg></div>
  <div class="hero-title abs"><span>HARBOUR CREST</span><strong>PHYSIOTHERAPY</strong></div>
</section>

<div class="welcome-photo abs" role="img" aria-label="Physiotherapist guiding a patient exercising on a gym ball with a resistance band"></div>
<section class="welcome-text abs">
  <h1>WELCOME TO<br>HARBOUR CREST PHYSIOTHERAPY</h1>
  <p>Harbour Crest Physiotherapy is an innovative physiotherapy practice offering comprehensive services by experienced and highly-qualified physiotherapists. We achieve outstanding clinical results for a broad range of common conditions including: back pain, neck pain, headache, migraine, shoulder pain, sports injuries, vertigo, knee pain, incontinence, persistent pelvic pain &amp; women's health and men's health issues.</p>
  <p>Our team of physiotherapists have extensive experience from working in private practice, private and public hospitals, and research and teaching over a range of physiotherapy disciplines including sports, manipulative, musculoskeletal, neurological</p>
  <span class="btn btn-green">BOOK ONLINE HERE</span>
</section>

<section class="services abs">
  <h2 class="section-title">OUR SERVICES</h2>
  <div class="service abs" style="left:110px;top:143px">
    <div class="icon"><svg width="60" height="60" viewBox="0 0 60 60" fill="#fff"><circle cx="36" cy="10" r="6"/><path d="M22 22l12-2 6 12 10 2-1 4-13-3-5-6-4 10 8 8-4 14h-5l3-12-9-7-6 10-10-2 2-4 6 1 8-17-6 2-4 6-4-2z"/></svg></div>
    <h3>PHYSIOTHERAPY</h3>
    <p>Our team of experienced physiotherapists have a wide range of specialities and are well placed to diagnose and manage your problem.</p>
  </div>
  <div class="service abs" style="left:440px;top:143px">
    <div class="icon"><svg width="60" height="70" viewBox="0 0 60 70" fill="#fff"><rect x="24" y="2" width="12" height="7" rx="2"/><rect x="23" y="12" width="14" height="7" rx="2"/><rect x="22" y="22" width="16" height="7" rx="2"/><rect x="21" y="32" width="18" height="7" rx="2"/><rect x="20" y="42" width="20" height="8" rx="2"/><rect x="19" y="53" width="22" height="9" rx="2"/></svg></div>
    <h3>CHRONIC PAIN MANAGEMENT</h3>
    <p>We all understand the complex nature of chronic pain and the need for a multidisciplinary, Biopsychosocial approach.</p>
  </div>
  <div class="service abs" style="left:770px;top:143px">
    <div class="icon"><svg width="60" height="70" viewBox="0 0 60 70" fill="#fff"><circle cx="30" cy="9" r="7"/><path d="M22 20h16l4 22h-6l-1 26h-5l-1-18-1 18h-5l-1-26h-6z"/><path d="M44 30l6 38" stroke="#fff" stroke-width="3"/></svg></div>
    <h3>KNEE CLINIC</h3>
    <p>The knee pain clinic provides a complete approach for those suffering from knee pain, recovering from knee surgery or knee injury.</p>
  </div>
  <div class="service abs" style="left:110px;top:428px">
    <div class="icon"><svg width="64" height="60" viewBox="0 0 64 60" fill="none" stroke="#fff" stroke-width="4"><rect x="6" y="8" width="44" height="30" rx="2"/><path d="M20 48h16M28 38v10M56 20v26a6 6 0 01-12 0"/></svg></div>
    <h3>REAL TIME ULTRASOUND</h3>
    <p>Physiotherapists use real-time ultrasound to examine how the small stabilising muscles of the spine are functioning.</p>
  </div>
  <div class="service abs" style="left:440px;top:428px">
    <div class="icon"><svg width="70" height="64" viewBox="0 0 70 64" fill="#fff"><circle cx="20" cy="8" r="7"/><circle cx="50" cy="8" r="7"/><path d="M14 18h12l3 18h-4v26h-5V44h-2v18h-5V36h-4z"/><path d="M44 18h12l8 26h-7v18h-5V46h-2v16h-5V44h-7z"/></svg></div>
    <h3>WOMEN'S &amp; MEN'S HEALTH</h3>
    <p>Our specialised Women's and Men's Health clinic is dedicated to addressing the often-distressing symptoms of incontinence, pelvic pain, and bladder and bowel dysfunction.</p>
  </div>
  <div class="service abs" style="left:770px;top:428px">
    <div class="icon"><svg width="64" height="60" viewBox="0 0 64 60"><circle cx="36" cy="20" r="15" fill="none" stroke="#fff" stroke-width="4"/><path d="M36 12v16M28 20h16" stroke="#fff" stroke-width="4"/><path d="M4 44l12-6h14l10 4 14-6 4 4-18 12H14l-10-4z" fill="#fff"/></svg></div>
    <h3>OTHER SERVICES</h3>
    <p>We have a range of other services available at Harbour Crest Physiotherapy. Click here for more information</p>
  </div>
</section>

<section class="practitioners abs">
  <h2 class="section-title">OUR PRACTITIONERS</h2>
  <p>All practitioners at our clinic have completed or are completing postgraduate university training and most are involved in teaching, university lecturing and research. This means that you are being treated by highly qualified people at the forefront of new developments in the management of musculoskeletal disorders.</p>
  <span class="btn btn-navy abs" style="left:539px;top:232px">READ MORE</span>
</section>

<h2 class="section-title blog-title abs">LATEST BLOG</h2>
<article class="post abs" style="left:99px;top:2438px">
  <div class="post-photo" role="img" aria-label="Therapist massaging a patient's back" style="background:linear-gradient(135deg,#e9b79a,#c98467 55%,#8c5240)"></div>
  <div class="post-date">SEP<br>09<br>2018</div>
  <h3>Nemo enim ipsam voluptatem quia</h3>
  <p>Sed ut perspiciatis unde omnis iste natus error sit uptatem accusantium doloremque laudantium, totam rem aperiam, eaque ipsa quae ab illo inventore veritatis</p>
</article>
<article class="post abs" style="left:443px;top:2438px">
  <div class="post-photo" role="img" aria-label="Physiotherapist stretching a woman on an exercise ball" style="background:linear-gradient(135deg,#f1e3ea,#d8a7bd 45%,#e9d85a 80%)"></div>
  <div class="post-date">SEP<br>09<br>2018</div>
  <h3>Nemo enim ipsam voluptatem quia</h3>
  <p>Sed ut perspiciatis unde omnis iste natus error sit uptatem accusantium doloremque laudantium, totam rem aperiam, eaque ipsa quae ab illo inventore veritatis</p>
</article>
<article class="post abs" style="left:788px;top:2438px">
  <div class="post-photo" role="img" aria-label="Nurse helping an older man exercise with a small ball" style="background:linear-gradient(135deg,#7cc3c3,#d9d3c8 55%,#e6c24a)"></div>
  <div class="post-date">SEP<br>09<br>2018</div>
  <h3>Nemo enim ipsam voluptatem quia</h3>
  <p>Sed ut perspiciatis unde omnis iste natus error sit uptatem accusantium doloremque laudantium, totam rem aperiam, eaque ipsa quae ab illo inventore veritatis</p>
</article>

<footer class="site-footer abs">
  <div class="footer-brand abs"><span class="brand-dot"></span>Harbour Crest Physiotherapy</div>
  <div class="social abs" style="left:136px"></div>
  <div class="social abs" style="left:180px"></div>

  <div class="abs" style="left:324px;top:50px;width:260px">
    <h4 class="col-title">CONTACT US</h4>
    <ul class="contact-list">
      <li><svg width="14" height="18" viewBox="0 0 14 18"><path d="M7 1a6 6 0 016 6c0 4-6 10-6 10S1 11 1 7a6 6 0 016-6z" fill="none" stroke="#333" stroke-width="1.6"/><circle cx="7" cy="7" r="2" fill="#333"/></svg><span>Harbour Crest Physiotherapy 18 Wattle Lane, Northvale, VIC 3999</span></li>
      <li><svg width="14" height="14" viewBox="0 0 24 24"><path fill="#333" d="M6.6 10.8a15 15 0 006.6 6.6l2.2-2.2a1 1 0 011-.25 11 11 0 003.6.6 1 1 0 011 1V20a1 1 0 01-1 1A17 17 0 013 4a1 1 0 011-1h3.5a1 1 0 011 1 11 11 0 00.6 3.6 1 1 0 01-.25 1z"/></svg><span>Phone: 1-800-555-0199</span></li>
      <li><svg width="14" height="12" viewBox="0 0 14 12"><rect x="0" y="1" width="14" height="10" fill="#333"/><path d="M0 1l7 5 7-5" stroke="#fff" stroke-width="1.2" fill="none"/></svg><span>hello@harbourcrestphysiotherapy.com.au</span></li>
    </ul>
  </div>

  <div class="newsletter abs" style="left:645px;top:50px;width:300px">
    <h4 class="col-title">SIGN UP FOR NEWSLETTER</h4>
    <p>Excepteur sint occaecat cupidatat non proident, sunt in culpa qui officia deserunt</p>
    <div class="email-field">Enter email</div>
    <span class="btn btn-sub">SUBSCRIPTION</span>
  </div>

  <div class="abs" style="left:976px;top:48px;width:130px">
    <h4 class="col-title">QUICK LINKS</h4>
    <ul class="quick-links"><li>Home</li><li>About</li><li>Service</li><li>Conditions</li><li>Health Tips</li><li>Blog</li><li>Contact</li></ul>
  </div>
</footer>
<div class="copyright abs">©2018 Harbour Crest Physiotherapy. All Rights Reserved.</div>

</body>
</html>
```